tri-fold brochure design for psychology practice - all content provided

we are a psychology practice that specialises in diagnostic and educational assessments for children, adolescents and adults. We have an existing logo and I am attaching a word doc (tri-fold brochure) with the required content. I am also attaching our logo and other relevant content docs. The layout is only a sample and we are looking for someone to put this together into a consistent and better layout.

Target Market(s)

parents

Industry/Entity Type

education and health

Font styles to use
Other font styles liked:
• crimsonpro

Requirements
Must have
• our logo and the provided content

```html
<!DOCTYPE html>
<html lang="en">
<head>
<meta charset="utf-8">
<title>brightfield – tri-fold brochure</title>
<link rel="stylesheet" href="https://fonts.googleapis.com/css2?family=Poppins:wght@300;400;600;700&display=swap">
<style>
  :root {
    --green: #5b9b39;
    --green-soft: rgba(91,155,57,0.88);
    --blue: #1d3f66;
    --ink: #1e1e1e;
    --charcoal: #2c2c2c;
    --grey-box: #d8d8d8;
    --paper: #ffffff;
    --backdrop: #d6d6d6;
    --photo-warm: #c9c2bb;
    --photo-light: #e6e4e2;
  }
  * { box-sizing: border-box; margin: 0; padding: 0; }
  html, body { width: 864px; height: 1200px; overflow: hidden; background: var(--backdrop); }
  body { position: relative; font-family: "Poppins", sans-serif; color: var(--ink); }

  .spread { position: absolute; left: 42px; width: 780px; height: 560px; background: var(--paper); box-shadow: 0 6px 18px rgba(0,0,0,0.18); overflow: hidden; }
  .spread--outside { top: 20px; }
  .spread--inside { top: 620px; }
  .spread__art { position: absolute; inset: 0; width: 780px; height: 560px; }
  .fold { position: absolute; top: 0; width: 1px; height: 560px; background: rgba(0,0,0,0.06); }

  .block { position: absolute; }
  .heading { font-weight: 700; font-size: 11px; color: var(--green); letter-spacing: 0.5px; text-transform: uppercase; display: flex; align-items: center; gap: 6px; }
  .heading--light { color: var(--paper); }
  .tick { width: 15px; height: 15px; flex: none; }
  .copy { font-size: 8.6px; line-height: 1.38; margin-top: 5px; }
  .copy--light { color: var(--paper); }

  .card-identify { left: 70px; top: 300px; width: 185px; height: 132px; background: var(--green); border-radius: 22px 8px 22px 8px; padding: 14px 14px; color: var(--paper); }

  .contact { left: 260px; top: 300px; width: 260px; text-align: center; font-size: 10px; line-height: 1.55; }
  .contact__name { font-weight: 700; color: var(--green); font-size: 12px; letter-spacing: 0.5px; }
  .contact__gap { height: 14px; }

  .brand { display: flex; align-items: center; gap: 5px; font-weight: 600; color: var(--green); font-size: 15px; }
  .brand__dot { width: 10px; height: 10px; border-radius: 50%; background: var(--green); }
  .brand-sub { font-size: 5.5px; color: #555; text-align: center; margin-top: 1px; }
  .brand-cover { left: 600px; top: 50px; width: 110px; display: flex; flex-direction: column; align-items: center; }

  .tagline { left: 520px; top: 300px; width: 260px; text-align: center; font-weight: 300; font-size: 17px; line-height: 1.2; color: var(--green); }
  .tagline__url { font-weight: 700; font-size: 9px; color: var(--ink); margin-top: 14px; }

  .who-title { left: 0; top: 30px; width: 260px; text-align: center; }
  .who-title .heading { justify-content: center; font-size: 12px; }
  .who-text { left: 22px; top: 355px; width: 215px; }

  .mission { left: 280px; top: 24px; width: 225px; }
  .mission__lead { font-weight: 700; font-size: 9.4px; line-height: 1.3; color: var(--green); font-style: normal; }

  .conditions { left: 340px; top: 360px; width: 165px; color: var(--paper); font-weight: 600; font-size: 7.6px; line-height: 1.45; text-transform: uppercase; list-style: none; }
  .conditions li::before { content: "• "; }

  .steps { left: 520px; top: 0; width: 260px; height: 440px; }
  .step { position: absolute; display: flex; gap: 8px; font-size: 8px; line-height: 1.35; }
  .step__num { font-weight: 700; font-size: 13px; color: var(--green); flex: none; width: 16px; }
  .step--boxed { background: var(--grey-box); border-radius: 18px 0 0 18px; padding: 9px 10px 9px 12px; }
  .step-rule { position: absolute; left: 28px; top: 14px; width: 14px; height: 2px; background: var(--green); }

  .brand-inside { left: 640px; top: 396px; display: flex; flex-direction: column; align-items: flex-end; }

  .closing { left: 520px; top: 440px; width: 260px; height: 120px; background: var(--charcoal); border-radius: 28px 0 0 0; padding: 18px 18px; color: var(--paper); font-size: 8.2px; line-height: 1.45; text-transform: uppercase; }
</style>
</head>
<body>

<!-- Outside spread -->
<section class="spread spread--outside">
  <svg class="spread__art" viewBox="0 0 780 560" aria-hidden="false">
    <defs>
      <linearGradient id="officeTones" x1="0" y1="0" x2="1" y2="1">
        <stop offset="0" stop-color="#eceae8"/>
        <stop offset="1" stop-color="#b9aea4"/>
      </linearGradient>
      <linearGradient id="sessionTones" x1="0" y1="0" x2="1" y2="0">
        <stop offset="0" stop-color="#e4e6ea"/>
        <stop offset="0.45" stop-color="#5d7594"/>
        <stop offset="1" stop-color="#1d3f66"/>
      </linearGradient>
    </defs>
    <path role="img" aria-label="Photo of a smiling psychologist in a bright office" fill="url(#officeTones)"
          d="M0 0 H260 V225 C200 190 120 175 0 200 Z"/>
    <path role="img" aria-label="Photo of a smiling boy playing with coloured blocks during an assessment session" fill="url(#sessionTones)"
          d="M260 0 H725 C705 70 745 130 745 200 C745 270 695 300 640 290 C570 280 520 225 440 235 C360 245 305 262 260 240 Z"/>
    <circle cx="655" cy="72" r="58" fill="#ffffff"/>
  </svg>
  <div class="fold" style="left:260px"></div>
  <div class="fold" style="left:520px"></div>

  <div class="block" style="left:20px; top:218px; width:235px;">
    <div class="heading"><svg class="tick" viewBox="0 0 16 16"><circle cx="8" cy="8" r="8" fill="#5b9b39"/><path d="M4.5 8.3 L7 10.6 L11.6 5.6" stroke="#fff" stroke-width="2" fill="none" stroke-linecap="round"/></svg>Understanding</div>
    <p class="copy">Assessment starts with listening first, and then asking the right questions in order to ensure that we are understanding your concerns and hearing your questions.</p>
  </div>

  <div class="block card-identify">
    <div class="heading heading--light"><svg class="tick" viewBox="0 0 16 16"><circle cx="8" cy="8" r="8" fill="#ffffff"/><path d="M4.5 8.3 L7 10.6 L11.6 5.6" stroke="#5b9b39" stroke-width="2" fill="none" stroke-linecap="round"/></svg>Identifying</div>
    <p class="copy copy--light">It is then our job to use our diagnostic and assessment knowledge and skills to collect the right data in order to address your concerns and provide answers to your questions.</p>
  </div>

  <div class="block" style="left:20px; top:450px; width:235px;">
    <div class="heading"><svg class="tick" viewBox="0 0 16 16"><circle cx="8" cy="8" r="8" fill="#5b9b39"/><path d="M4.5 8.3 L7 10.6 L11.6 5.6" stroke="#fff" stroke-width="2" fill="none" stroke-linecap="round"/></svg>Guiding</div>
    <p class="copy">This then enables us to provide you with recommendations for accessing support and interventions that are based on current best practice and are supported by evidence.</p>
  </div>

  <div class="block contact">
    <p class="contact__name">BRIGHTFIELD</p>
    <p>12/48 Harbour View Rd,<br>Seaview NSW 2100</p>
    <div class="contact__gap"></div>
    <p>info@brightfieldassess.com.au</p>
    <p>www.brightfieldassess.com.au</p>
    <p>ph: 02 9000 4127</p>
  </div>

  <div class="block brand-cover">
    <div class="brand"><span class="brand__dot"></span>brightfield</div>
    <p class="brand-sub">diagnostic and educational assessments</p>
  </div>

  <div class="block tagline">
    <p>UNDERSTANDING<br>IDENTIFYING<br>GUIDING</p>
    <p class="tagline__url">www.brightfieldassess.com.au</p>
  </div>
</section>

<!-- Inside spread -->
<section class="spread spread--inside">
  <svg class="spread__art" viewBox="0 0 780 560">
    <defs>
      <linearGradient id="familyTones" x1="0" y1="0" x2="1" y2="1">
        <stop offset="0" stop-color="#eef0f1"/>
        <stop offset="1" stop-color="#d9b9a6"/>
      </linearGradient>
      <linearGradient id="counselTones" x1="0" y1="0" x2="1" y2="0">
        <stop offset="0" stop-color="#d8d6d3"/>
        <stop offset="0.6" stop-color="#8f8b86"/>
        <stop offset="1" stop-color="#4a4846"/>
      </linearGradient>
    </defs>
    <circle role="img" aria-label="Photo of a mother helping her young son with drawing" cx="130" cy="155" r="88" fill="url(#familyTones)"/>
    <path role="img" aria-label="Photo of a counsellor talking with a teenager on a couch" fill="url(#counselTones)"
          d="M0 300 C100 275 200 270 290 262 C360 256 380 222 450 222 C500 222 520 262 520 300 V560 H0 Z"/>
    <path fill="#5b9b39" fill-opacity="0.88"
          d="M0 325 C80 305 190 298 245 330 C290 360 285 460 262 560 H0 Z"/>
    <circle cx="425" cy="420" r="92" fill="#5b9b39"/>
  </svg>
  <div class="fold" style="left:260px"></div>
  <div class="fold" style="left:520px"></div>

  <div class="block who-title"><p class="heading">Who we are</p></div>

  <div class="block who-text">
    <p class="copy copy--light">brightfield is a team with a passion for helping people to thrive. We are a team of psychologists and teachers who have experience in both educational and clinical settings.</p>
    <p class="copy copy--light" style="margin-top:9px">We understand the challenges parents face in wanting what is best for their children, trying to understand how and where to access the most relevant information and support.</p>
  </div>

  <div class="block mission">
    <p class="mission__lead">We are passionate about wanting to help families navigate the diagnostic and assessment process.</p>
    <p class="copy" style="margin-top:9px">We believe that quality and comprehensive assessment needs to happen before intervention begins. We work collaboratively with other professionals to ensure that recommendations and supports put in place are appropriate and evidence-based while also meeting the needs of the individual.</p>
    <p class="copy" style="margin-top:8px">We are qualified to give formal diagnoses for mental health conditions and specific learning disorders. This includes:</p>
  </div>

  <ul class="block conditions">
    <li>Attention Deficit Hyperactivity Disorder</li>
    <li>Autism Spectrum Disorders</li>
    <li>Specific Learning Disorders</li>
    <li>Language Disorders</li>
    <li>Anxiety Disorders</li>
    <li>Mood Disorders</li>
    <li>Communication Disorders</li>
  </ul>

  <div class="block steps">
    <span class="step-rule"></span>
    <div class="step" style="left:22px; top:28px; width:200px;"><span class="step__num">1.</span><p>An initial face-to-face interview to discuss your concerns and understand the relevant history and details.</p></div>
    <div class="step step--boxed" style="left:60px; top:92px; width:200px;"><span class="step__num">2.</span><p>A formal assessment session during which relevant tests are completed. This can include IQ testing, Achievement testing, Memory testing, Personality profiling etc.</p></div>
    <div class="step" style="left:22px; top:180px; width:210px;"><span class="step__num">3.</span><p>Obtaining additional information through questionnaires, observation, contact with other professionals (such as teachers/tutors etc).</p></div>
    <div class="step step--boxed" style="left:60px; top:245px; width:200px;"><span class="step__num">4.</span><p>A feedback session during which we provide you with a final draft of the report and discuss possible recommendations, collaborating about the next steps.</p></div>
    <div class="step" style="left:22px; top:330px; width:200px;"><span class="step__num">5.</span><p>A copy of the finalised report is provided and opportunity for discussion and engagement with teachers or other allied health is provided.</p></div>
  </div>

  <div class="block brand-inside">
    <div class="brand"><span class="brand__dot"></span>brightfield</div>
    <p class="brand-sub">diagnostic and educational assessments</p>
  </div>

  <div class="block closing">
    <p>We are passionate about collaborating with your school or workplace, supporting you in applying for financial support if available (such as NDIS funding), and to feel more informed and confident in your decisions.</p>
  </div>
</section>

</body>
</html>
```